Valtora

Standard Business Card design.
Sample two-sided design uploaded. White front, Black back.
Would like white shield to be on all black background side.
Willing to look at a couple creative designs, but nothing crazy.
Preference for a classic, confident, strong design.

```html
<!DOCTYPE html>
<html lang="en">
<head>
<meta charset="UTF-8">
<title>Valtora Business Card</title>
<link rel="stylesheet" href="https://fonts.googleapis.com/css2?family=Poppins:wght@400;600;700&display=swap">
<style>
  :root {
    --backdrop: #1e1e1e;
    --card-black: #0b0b0b;
    --card-white: #ffffff;
    --ink-light: #ffffff;
    --ink-dark: #111111;
    --rule: #8a8a8a;
  }
  * { margin: 0; padding: 0; box-sizing: border-box; }
  html, body { width: 1200px; height: 900px; overflow: hidden; }
  body {
    background: var(--backdrop);
    font-family: "Poppins", sans-serif;
    position: relative;
  }
  .card {
    position: absolute;
    left: 280px;
    width: 640px;
    height: 366px;
    border-radius: 3px;
    box-shadow: 0 18px 40px rgba(0,0,0,0.55);
  }
  .card-front { top: 54px; background: var(--card-white); }
  .card-back { top: 480px; background: var(--card-black); color: var(--ink-light); }

  .brand {
    display: flex;
    align-items: center;
    gap: 14px;
    font-weight: 600;
    letter-spacing: 0.14em;
    text-transform: uppercase;
    white-space: nowrap;
  }
  .brand-square { width: 22px; height: 22px; }
  .card-front .brand {
    position: absolute; left: 50%; top: 50%;
    transform: translate(-50%, -50%);
    font-size: 44px; color: var(--ink-dark);
  }
  .card-front .brand-square { background: var(--ink-dark); }

  .card-back .brand {
    position: absolute; left: 44px; top: 50%;
    transform: translateY(-50%);
    font-size: 34px; color: var(--ink-light);
  }
  .card-back .brand-square { background: var(--ink-light); width: 18px; height: 18px; }

  .divider {
    position: absolute; left: 334px; top: 96px;
    width: 1px; height: 190px; background: var(--rule);
  }
  .contact {
    position: absolute; left: 362px; top: 86px;
    font-size: 14px; line-height: 1.35;
    white-space: nowrap;
  }
  .contact-name { font-weight: 700; font-size: 19px; letter-spacing: 0.03em; text-transform: uppercase; }
  .contact-title { font-size: 14px; margin-bottom: 12px; }
  .contact-list { list-style: none; }
  .contact-list li { display: flex; align-items: center; gap: 8px; font-size: 15px; }
  .contact-list svg { width: 14px; height: 14px; flex: none; }
  .contact-address { margin-top: 12px; font-size: 15px; line-height: 1.3; }
</style>
</head>
<body>
  <section class="card card-front" aria-label="Card front">
    <div class="brand"><span class="brand-square"></span>Valtora</div>
  </section>

  <section class="card card-back" aria-label="Card back">
    <div class="brand"><span class="brand-square"></span>Valtora</div>
    <div class="divider"></div>
    <div class="contact">
      <p class="contact-name">Marcus Hale</p>
      <p class="contact-title">Managing Director</p>
      <ul class="contact-list">
        <li>
          <svg viewBox="0 0 24 24" fill="none" stroke="#fff" stroke-width="2"><path d="M5 3h4l2 5-3 2a12 12 0 0 0 6 6l2-3 5 2v4a2 2 0 0 1-2 2A18 18 0 0 1 3 5a2 2 0 0 1 2-2z"/></svg>
          044-310 872 564
        </li>
        <li>
          <svg viewBox="0 0 24 24" fill="none" stroke="#fff" stroke-width="2"><rect x="2" y="5" width="20" height="14"/><path d="M2 5l10 8 10-8"/></svg>
          info@valtora.com
        </li>
        <li>
          <svg viewBox="0 0 24 24" fill="none" stroke="#fff" stroke-width="2"><circle cx="12" cy="12" r="10"/><path d="M2 12h20M12 2c3 3 3 17 0 20M12 2c-3 3-3 17 0 20"/></svg>
          www.valtora.com
        </li>
      </ul>
      <p class="contact-address">18, Harlow Street Westbury<br>72018, Eastland</p>
    </div>
  </section>
</body>
</html>
```